Flyer Tally Desk Ledger Kit

Hi
Can you please design me a DL Flyer for: Tally Desk Ledger Kit
Info:
Starting a new Business ?
Want to save on bookkeeping fees for your existing business?

You can now save 1000's off bookkeeping fees by Doing it Yourself.

Using our Bookkeeper software you simply key in the information as you go.

We offer one on one training, backup and support.
We can assist you with BAS Preparation and Payrol Advice.

Add Modules as required:
Point of Sale Module
Jobs Management Module
Website Intergration Module

Fee set up assistance and training.

Lets get the ball rolling: 1300 462 815
www.tldlk.com.au
admin@tldlk.com.au (use the logo thing you made)

Target Market(s)

Small Business

Colors
ec1f27
f04a50
f59296
fcdcdc
ffffff

Requirements
Nice to have
• image/s related to bookkeeping

```html
<!DOCTYPE html>
<html lang="en">
<head>
<meta charset="utf-8">
<title>Tally Desk Ledger Kit – DL Flyer</title>
<link rel="stylesheet" href="https://fonts.googleapis.com/css2?family=Didact+Gothic&family=Poppins:wght@500;600;700&family=EB+Garamond:ital@1&display=swap">
<style>
  :root {
    --red: #ec1f27;
    --red-soft: #f04a50;
    --pink: #f59296;
    --blush: #fcdcdc;
    --white: #ffffff;
    --ink: #3f3f42;
    --rule: #8a8a8e;
    --stage: #d4d5da;
  }
  * { margin: 0; padding: 0; box-sizing: border-box; }
  html, body { width: 1108px; height: 1200px; overflow: hidden; }
  body { background: var(--stage); position: relative; font-family: "Didact Gothic", sans-serif; color: var(--ink); }

  .panel { position: absolute; top: 145px; width: 437px; height: 928px; background: var(--white); overflow: hidden; }
  .panel--front { left: 73px; }
  .panel--back { left: 602px; }

  /* front */
  .hero-photo { position: absolute; left: 0; top: 0; width: 300px; height: 860px;
    background: linear-gradient(180deg, #c9b8a6 0%, #e8e1d9 30%, #f1eee9 60%, #dcd7d0 100%); }
  .hero-fade { position: absolute; left: 200px; top: 0; width: 237px; height: 928px;
    background: linear-gradient(90deg, rgba(255,255,255,0) 0%, #f5f6f9 45%, #e6e8ee 100%); }
  .front-copy { position: absolute; left: 210px; width: 205px; top: 32px; text-align: center; font-family: "Poppins", sans-serif; font-weight: 600; }
  .front-copy .q { font-size: 31px; line-height: 33px; }
  .front-copy .red { color: var(--red); }
  .front-copy .dark { color: var(--ink); }
  .front-copy hr { border: 0; border-top: 1px solid var(--rule); margin: 12px 5px 12px; }
  .front-copy .s { font-size: 20px; line-height: 32px; }
  .front-copy .s.dark { font-size: 18px; font-weight: 500; }

  .brand-block { position: absolute; left: 30px; top: 762px; width: 390px; }
  .brand-name { font-family: "Poppins", sans-serif; font-weight: 600; color: var(--red); font-size: 33px; line-height: 40px; }
  .tagline { font-family: "EB Garamond", serif; font-style: italic; font-size: 21px; color: var(--ink); margin-top: 4px; }
  .web { position: absolute; left: 72px; top: 883px; display: flex; align-items: center; gap: 8px; color: var(--red); font-size: 25px; }

  /* back */
  .binder-photo { position: absolute; inset: 0;
    background: linear-gradient(110deg, #f4f4f4 0%, #f4f4f4 50%, var(--blush) 62%, #f8c9cb 80%, var(--blush) 100%); }
  .back-copy { position: absolute; left: 52px; top: 88px; width: 340px; }
  .headline { font-family: "Poppins", sans-serif; font-weight: 600; color: var(--ink); }
  .headline .l1 { font-size: 47px; line-height: 52px; letter-spacing: -0.5px; }
  .headline .l2 { font-size: 53px; line-height: 54px; }
  .headline .l3 { font-size: 29px; line-height: 38px; }
  .headline .l4 { font-size: 33px; line-height: 46px; color: var(--red); font-weight: 700; }
  .back-copy hr { border: 0; border-top: 1px solid var(--rule); margin: 16px 0 22px; }
  .back-copy .brand-name { font-size: 34px; }
  .body-text { font-size: 16px; line-height: 20px; margin-top: 18px; }
  .body-text p + p { margin-top: 20px; }
  .modules { display: flex; align-items: center; gap: 16px; margin-top: 16px; }
  .modules ul { list-style: none; }
  .cta { font-family: "Poppins", sans-serif; font-weight: 600; font-size: 28px; line-height: 36px; }
  .phone { display: flex; align-items: center; gap: 6px; color: var(--red); font-family: "Poppins", sans-serif; font-weight: 700; font-size: 45px; line-height: 56px; }
  .email { display: flex; align-items: center; gap: 14px; font-size: 28px; line-height: 36px; margin-left: -6px; }
</style>
</head>
<body>

<section class="panel panel--front">
  <div class="hero-photo" role="img" aria-label="Photo of a young businesswoman in glasses at her desk"></div>
  <div class="hero-fade"></div>

  <div class="front-copy">
    <div class="q red">Starting<br>a new</div>
    <div class="q dark">business?</div>
    <hr>
    <div class="s red">Want to save on</div>
    <div class="s dark">bookkeeping fees</div>
    <div class="s red">for your existing<br>business?</div>
  </div>

  <div class="brand-block">
    <div class="brand-name">Tally Desk Ledger Kit</div>
    <div class="tagline">It's easy enough to do yourself</div>
  </div>

  <div class="web">
    <svg width="22" height="22" viewBox="0 0 22 22" fill="none" stroke="currentColor" stroke-width="1.8" aria-hidden="true">
      <circle cx="11" cy="11" r="9.5"/><ellipse cx="11" cy="11" rx="4" ry="9.5"/><line x1="1.5" y1="11" x2="20.5" y2="11"/><line x1="3" y1="6" x2="19" y2="6"/><line x1="3" y1="16" x2="19" y2="16"/>
    </svg>
    <span>www.tldlk.com.au</span>
  </div>
</section>

<section class="panel panel--back">
  <div class="binder-photo" role="img" aria-label="Soft photo of a red ring binder on an office desk"></div>

  <div class="back-copy">
    <div class="headline">
      <div class="l1">You can now</div>
      <div class="l2">save 1000's</div>
      <div class="l3">off bookkeeping fees</div>
      <div class="l4">by Doing it Yourself.</div>
    </div>
    <hr>
    <div class="brand-name">Tally Desk Ledger Kit</div>
    <div class="tagline">It's easy enough to do yourself</div>

    <div class="body-text">
      <p>Using our Bookkeeper software you simply key in the information as you go.</p>
      <p>We offer one on one training, backup and support.<br>We can assist you with BAS Preparation and Payrol Advice.</p>
      <p>Add Modules as required:</p>
    </div>
    <div class="modules body-text">
      <svg width="74" height="62" viewBox="0 0 74 62" aria-hidden="true">
        <g fill="none" stroke="var(--ink)" stroke-width="4">
          <rect x="2" y="2" width="19" height="58"/><rect x="27" y="2" width="19" height="58"/><rect x="52" y="2" width="19" height="58"/>
        </g>
        <g fill="var(--ink)"><rect x="2" y="46" width="19" height="14"/><rect x="27" y="46" width="19" height="14"/><rect x="52" y="46" width="19" height="14"/></g>
        <g fill="var(--white)"><circle cx="11.5" cy="53" r="3.5"/><circle cx="36.5" cy="53" r="3.5"/><circle cx="61.5" cy="53" r="3.5"/></g>
      </svg>
      <ul>
        <li>Point of Sale Module</li>
        <li>Jobs Management Module</li>
        <li>Website Intergration Module</li>
      </ul>
    </div>
    <div class="body-text"><p>Fee set up assistance and training.</p></div>
    <hr>
    <div class="cta">Lets get the ball rolling:</div>
    <div class="phone">
      <svg width="20" height="32" viewBox="0 0 20 32" aria-hidden="true"><rect x="2" y="2" width="16" height="28" rx="3" fill="none" stroke="var(--red)" stroke-width="3"/><circle cx="10" cy="25" r="1.8" fill="var(--red)"/></svg>
      <span>1300 462 815</span>
    </div>
    <div class="email">
      <svg width="24" height="18" viewBox="0 0 24 18" aria-hidden="true"><rect width="24" height="18" fill="var(--red)"/><path d="M1 1 L12 10 L23 1" fill="none" stroke="var(--white)" stroke-width="2"/></svg>
      <span>admin@tldlk.com.au</span>
    </div>
  </div>
</section>

</body>
</html>
```